Letterhead creation for military law attorney

I need letterhead design for my business. We are now only doing military law and need to change address, logo and vision. I like the idea of using an eagle or a jolly roger flag

Target Market(s)

Military Law Clients

Colors
3176b5
85abd2

Requirements
Must have
• We are defending people against the government
Nice to have
• Jolly Roger Flag

```html
<!DOCTYPE html>
<html lang="en">
<head>
<meta charset="utf-8">
<title>Ironvale Defense Law — Letterhead</title>
<link rel="stylesheet" href="https://fonts.googleapis.com/css2?family=Poppins:wght@400;500;600;700&display=swap">
<style>
  :root {
    --blue: #3176b5;
    --light-blue: #85abd2;
    --charcoal: #333335;
    --ink: #2b2b2d;
    --paper: #ffffff;
    --backdrop: #0b1a22;
  }
  * { box-sizing: border-box; margin: 0; padding: 0; }
  html, body { width: 1200px; height: 1070px; overflow: hidden; }
  body {
    background: radial-gradient(circle at 20% 60%, #103040 0%, var(--backdrop) 55%, #050b10 100%);
    font-family: "Poppins", sans-serif;
    color: var(--ink);
  }
  .letterhead {
    position: absolute;
    left: 200px; top: 20px;
    width: 800px; height: 1030px;
    background: var(--paper);
    overflow: hidden;
    box-shadow: 0 10px 40px rgba(0,0,0,.5);
  }
  .letterhead__frame { position: absolute; inset: 0; }
  .brand {
    position: absolute; left: 78px; top: 172px;
    display: flex; align-items: center; gap: 12px;
    font-weight: 600; font-size: 22px; color: var(--blue);
  }
  .brand__mark { width: 18px; height: 18px; background: var(--blue); }
  .contact {
    position: absolute; left: 565px; top: 138px;
    list-style: none; font-size: 11.5px; line-height: 1.35;
  }
  .contact__item { display: flex; align-items: center; gap: 8px; margin-bottom: 14px; }
  .contact__icon {
    width: 22px; height: 22px; background: var(--blue);
    display: flex; align-items: center; justify-content: center; flex: none;
  }
  .divider { position: absolute; left: 98px; top: 285px; }
  .date {
    position: absolute; right: 105px; top: 340px;
    font-weight: 600; font-size: 19px;
  }
  .recipient {
    position: absolute; left: 110px; top: 375px;
    font-size: 19px; line-height: 1.3;
  }
  .recipient strong { display: block; font-weight: 600; }
  .body-copy {
    position: absolute; left: 112px; top: 470px; width: 590px;
    font-size: 15.5px; line-height: 1.62; text-align: justify;
  }
  .body-copy p { margin-bottom: 24px; }
</style>
</head>
<body>
  <article class="letterhead">
    <svg class="letterhead__frame" width="800" height="1030" viewBox="0 0 800 1030" aria-hidden="true">
      <!-- header bands -->
      <rect x="0" y="0" width="800" height="100" fill="var(--charcoal)"/>
      <rect x="0" y="52" width="475" height="3" fill="var(--light-blue)"/>
      <rect x="0" y="78" width="475" height="22" fill="var(--blue)"/>
      <rect x="475" y="58" width="325" height="50" fill="var(--light-blue)"/>
      <!-- side bars -->
      <rect x="768" y="0" width="32" height="930" fill="var(--light-blue)"/>
      <rect x="0" y="150" width="22" height="830" fill="var(--blue)"/>
      <!-- footer bands -->
      <rect x="0" y="950" width="415" height="30" fill="var(--blue)"/>
      <rect x="415" y="930" width="385" height="30" fill="var(--light-blue)"/>
      <rect x="415" y="960" width="385" height="20" fill="var(--charcoal)"/>
      <rect x="415" y="975" width="385" height="3" fill="var(--blue)"/>
      <rect x="0" y="980" width="800" height="50" fill="var(--charcoal)"/>
    </svg>

    <div class="brand"><span class="brand__mark"></span>Ironvale Defense Law</div>

    <ul class="contact">
      <li class="contact__item">
        <span class="contact__icon"><svg width="10" height="14" viewBox="0 0 10 14"><rect x="1" y="1" width="8" height="12" rx="1.5" fill="none" stroke="#fff" stroke-width="1.4"/></svg></span>
        (555)014-2280
      </li>
      <li class="contact__item">
        <span class="contact__icon"><svg width="14" height="12" viewBox="0 0 14 12"><path d="M1 5 Q7 -1 13 5 L11 11 H3 Z" fill="#fff"/></svg></span>
        (555)014-2281
      </li>
      <li class="contact__item">
        <span class="contact__icon"><svg width="12" height="14" viewBox="0 0 12 14"><path d="M6 13 C2 8 1 6 1 5 A5 5 0 0 1 11 5 C11 6 10 8 6 13Z" fill="#fff"/><circle cx="6" cy="5" r="1.8" fill="var(--blue)"/></svg></span>
        PO Box 310 Marlow Springs,<br>TN 30917
      </li>
    </ul>

    <svg class="divider" width="610" height="6" viewBox="0 0 610 6" aria-hidden="true">
      <rect x="0" y="2" width="610" height="1.5" fill="var(--light-blue)"/>
      <rect x="235" y="1" width="115" height="3.5" fill="var(--blue)"/>
    </svg>

    <div class="date">DATE: 15.08.2019</div>

    <div class="recipient">To<strong>LOREM IPSUM</strong><strong>simply dummy text</strong></div>

    <div class="body-copy">
      <p>Lorem Ipsum is simply dummy text of the printing and typesetting industry. Lorem Ipsum has been the industry's standard dummy text ever since the 1500s, when an unknown printer took a galley of type and scrambled it to make a type specimen book. It has survived not only five centuries, but also the leap into electronic typesetting, remaining essentially unchanged. It was popularised in the 1960s with the release of Brightwell sheets containing Lorem Ipsum passages, and more recently with desktop publishing software like Quillset Pagecraft including versions of Lorem Ipsum.</p>
      <p>Lorem Ipsum is simply dummy text of the printing and typesetting industry. Lorem Ipsum has been the industry's standard dummy text ever since the 1500s, when an unknown printer took a galley of type and scrambled it to make a type specimen book. It has survived not only five centuries, but also the leap into electronic typesetting, remaining essentially unchanged.</p>
      <p>It was popularised in the 1960s with the release of Brightwell sheets containing Lorem Ipsum passages, and more recently with desktop publishing software like Quillset Pagecraft including versions of Lorem Ipsum.</p>
    </div>
  </article>
</body>
</html>
```